Business Card Project for Firm Deck Hoisting

Business name is "Firm Deck Hoisting" we are a scaffolding & rigging business specialising in local and remote work for:
- scaffolding (residential, commercial, industrial)
- rigging
-man material hoists
- swing stages
- labour hire

On the back of the card I would like FDH as the symbol / logo. I have attached the logos we have had created by sketch harbour. We would like to use bold colours – preferably as the same colour scheme as the logo.

Target Market(s)

Construction business

Industry/Entity Type

Construction

Contact Information for Business Card

name: Owen Pellew
Title: Director
Phone: 0491 572 864
Address: PO BOX 3251, Paralowie SA 5108
Email: owen@firmdeckhoisting.com.au
Website: www.firmdeckhoisting.com.au

Font styles to use
Sans Serif

Requirements
Must have
• Must use existing logo & prefering using bold colours
Nice to have
• Would be nice to have a line of dot points in what we specialise in but not essential
• Would be nice to see some designs with a slogan but not essential
Should not have
• NA

```html
<!DOCTYPE html>
<html lang="en">
<head>
<meta charset="utf-8">
<title>Firm Deck Hoisting — Business Card</title>
<link href="https://fonts.googleapis.com/css2?family=Lato:wght@400;700;900&display=swap" rel="stylesheet">
<style>
  :root {
    --brand-blue: #1a75bb;
    --back-blue: #1277bf;
    --ink: #1a1a1a;
    --paper: #ffffff;
    --stage: #e9ebee;
  }
  * { margin: 0; padding: 0; box-sizing: border-box; }
  html, body {
    width: 1007px; height: 1200px; overflow: hidden;
    background: var(--stage);
    font-family: "Lato", Arial, sans-serif;
  }
  .card {
    position: absolute; left: 118px; width: 752px; height: 428px; overflow: hidden;
  }
  /* front */
  .card--front {
    top: 148px; background: var(--paper);
    border-radius: 36px 0 36px 0;
  }
  .brand {
    position: absolute; left: 0; right: 0; top: 106px;
    display: flex; justify-content: center; align-items: center; gap: 14px;
    color: var(--brand-blue); font-weight: 900; font-size: 38px; letter-spacing: 1px;
  }
  .brand__square { width: 22px; height: 22px; background: var(--brand-blue); }
  .person__name {
    position: absolute; left: 61px; top: 211px;
    color: var(--brand-blue); font-weight: 700; font-size: 26px; letter-spacing: 0.3px;
  }
  .person__title {
    position: absolute; left: 61px; top: 243px;
    color: var(--ink); font-weight: 700; font-size: 21px;
  }
  .person__rule {
    position: absolute; left: 155px; width: 535px; top: 257px; height: 3px;
    background: var(--brand-blue);
  }
  .contact {
    position: absolute; color: var(--ink); font-size: 19px; line-height: 27px;
  }
  .contact--list { left: 60px; top: 291px; }
  .contact__row { display: flex; align-items: center; gap: 10px; }
  .contact__row svg { width: 20px; height: 18px; flex: none; }
  .contact--address { left: 491px; top: 318px; display: flex; gap: 6px; }
  .contact--address svg { width: 12px; height: 18px; margin-top: 4px; }
  .front-band {
    position: absolute; left: 0; right: 0; bottom: 0; height: 32px; background: var(--brand-blue);
  }
  .front-band__dark {
    position: absolute; left: 0; bottom: 0; width: 404px; height: 24px;
    background: var(--ink); border-top-right-radius: 24px;
    box-shadow: 0 0 0 4px var(--paper);
  }
  /* back */
  .card--back {
    top: 641px; background: var(--back-blue);
    border-radius: 0 36px 0 36px; color: var(--paper);
  }
  .back__mark {
    position: absolute; left: 64px; top: 148px;
    font-weight: 900; font-size: 98px; letter-spacing: 2px; line-height: 1;
  }
  .back__divider {
    position: absolute; left: 336px; top: 108px; width: 3px; height: 224px; background: var(--paper);
  }
  .services {
    position: absolute; left: 356px; top: 118px; list-style: none; font-size: 20px; line-height: 25px;
  }
  .services li { position: relative; padding-left: 16px; margin-bottom: 11px; }
  .services li::before {
    content: ""; position: absolute; left: 0; top: 9px; width: 10px; height: 10px;
    border-radius: 50%; background: var(--paper);
  }
  .back__web {
    position: absolute; left: 0; right: 0; top: 366px; text-align: center;
    font-size: 20px; letter-spacing: 1.4px;
  }
</style>
</head>
<body>
  <section class="card card--front">
    <div class="brand"><span class="brand__square"></span><span>FIRM DECK HOISTING</span></div>
    <h1 class="person__name">OWEN PELLEW</h1>
    <p class="person__title">Director</p>
    <div class="person__rule"></div>
    <div class="contact contact--list">
      <div class="contact__row">
        <svg viewBox="0 0 20 18"><path fill="#1a75bb" d="M2 6c0-3 3-5 8-5s8 2 8 5v1h-4V5H6v2H2zM5 8h10l3 8H2z"/><circle cx="10" cy="12" r="2" fill="#fff"/></svg>
        <span>0491 572 864</span>
      </div>
      <div class="contact__row">
        <svg viewBox="0 0 20 18"><rect x="1.5" y="3.5" width="17" height="11" fill="none" stroke="#1a75bb" stroke-width="2"/><path d="M2 4l8 6 8-6" fill="none" stroke="#1a75bb" stroke-width="2"/></svg>
        <span>owen@firmdeckhoisting.com.au</span>
      </div>
      <div class="contact__row">
        <svg viewBox="0 0 20 18"><circle cx="10" cy="9" r="7.5" fill="none" stroke="#1a75bb" stroke-width="2"/><path d="M2.5 9h15M10 1.5c-4 4-4 11 0 15M10 1.5c4 4 4 11 0 15" fill="none" stroke="#1a75bb" stroke-width="1.5"/></svg>
        <span>www.firmdeckhoisting.com.au</span>
      </div>
    </div>
    <div class="contact contact--address">
      <svg viewBox="0 0 12 18"><path fill="#1a75bb" d="M6 0a6 6 0 0 1 6 6c0 4-6 12-6 12S0 10 0 6a6 6 0 0 1 6-6z"/><circle cx="6" cy="6" r="2.3" fill="#fff"/></svg>
      <span>PO BOX 3251,<br>Northvale SA 5190</span>
    </div>
    <div class="front-band"></div>
    <div class="front-band__dark"></div>
  </section>

  <section class="card card--back">
    <div class="back__mark">FDH</div>
    <div class="back__divider"></div>
    <ul class="services">
      <li>scaffolding<br>(residential, commercial, industrial)</li>
      <li>rigging</li>
      <li>man material hoists</li>
      <li>swing stages</li>
      <li>labour hire</li>
    </ul>
    <p class="back__web">www.firmdeckhoisting.com.au</p>
  </section>
</body>
</html>
```